Costume Store Needs Redesign/Modern Website

We have a local retail store of costumes, accessories, wigs, makeup, masks, etc.

The original idea behind the website was to give people an incentive for coming to the store by giving them an idea of the size of the store, the large variety of products and the overall appeal of the store.

While pursuing this objective, however,  the website became too cluttered and hard to navigate. We would like to keep this original goal but have a much cleaner & professional presentation.

At this point we don't sell online, so showing a clear picture of what a customer could find here in the store is really what we want to accomplish.

With that in mind, I would like to add a section in the navigation menu titled "Ordering". Customers often get confused on the website and end up calling the store asking where the "cart" is and they can't figure out how to order online because it's not clear enough that we only sell in store. Here's an example of a website I found that doesn't sell online but has an "Ordering" link that explains the options for the customer: https://www.corvelshopwares.example/ordering/

Another thing I would like for the homepage, is some google reviews to be featured as a slideshow. I found an example here at the bottom of the page: http://www.maritapellones.example/

I like the overall look of that website as well.

Here is one more example of a website I really like the design of: http://www.brakefordhls.example/.

What I like about it is the big slideshow of pictures at the top of the homepage, the simplicity, and the navigation.

We need to try to get attention with pictures and fewer words, especially for the Homepage. Keep the longer descriptions inside the specific sections.

For the Homepage, I'd like a few main categories listed as picture links, with a few words to the right of the image to describe what they will find in that section.

The categories I'm thinking for the homepage are,

1. “Featured" this section would change seasonally but at the moment St. Patricks Day would be what that section would link to.

2. Next would be "Costumes" and once you click that picture have it link to a page that lists the categories of costumes we feature on the website ( holiday, renaissance, decade, etc.).

Other main categories for the homepage could be "Lingerie Boutique", "Gifts and Oils", "Wigs", "Makeup". Even with the picture links, I would still like to keep the navigation links at the top of the page even if they are duplicate to the pages we are linking to through the pictures on the homepage. This is just an idea, I would like to see your takes as well I'm open to suggestions for an outside perspective.

The main idea though is to make the homepage less wordy and less confusing.
Updates

We would like to see a design that looks like this; http://www.maritapellones.example/ With this Image as the background; https://www.filetandy.example/s/47kq21zp9vmtrba/508274_2018-Store-front-New-Final.jpg?dl=0

Target Market(s)

Local costume buyers

Industry/Entity Type

Store

Number of Pages Required

5+ page

Colors

Designer to choose colors to be used in the design.

Requirements
Must have
• I would like these 5 pages designed: Home, About us, Ordering, Merchandise, Videos

```html
<!DOCTYPE html>
<html lang="en">
<head>
<meta charset="utf-8">
<title>Guiseworks Costume Hall</title>
<link href="https://fonts.googleapis.com/css2?family=Montserrat:wght@500;600&family=Lato:ital,wght@0,400;0,700;1,400&display=swap" rel="stylesheet">
<style>
:root{
  --black:#000;
  --ink:#111;
  --footer-dark:#2b2b2b;
  --orange:#f39200;
  --orange-light:#fbb034;
  --green:#7dc242;
  --green-light:#9ad25a;
  --white:#fff;
  --grey-band:#e9e9e9;
  --caption:rgba(20,20,20,.82);
  --star:#f6c400;
}
*{box-sizing:border-box;margin:0;padding:0}
html,body{width:1200px;height:2228px;overflow:hidden;background:var(--white)}
body{position:relative;font-family:'Lato',sans-serif;color:var(--ink)}
.abs{position:absolute}

/* header */
.site-header{left:0;top:0;width:1200px;height:123px;background:var(--black)}
.brand{left:143px;top:30px;display:flex;align-items:center;gap:12px;color:var(--green);font-family:'Lato',sans-serif;font-weight:700;font-size:32px}
.brand-dot{width:26px;height:26px;border-radius:50%;background:var(--orange)}
.social{display:flex;gap:8px}
.social span{width:34px;height:34px;border:2px solid var(--white);border-radius:50%;display:block}
.header-social{left:809px;top:20px}
.contact-line{display:flex;align-items:center;gap:8px;color:var(--white);font-family:'Lato',sans-serif;font-weight:700;font-size:18px}
.header-address{left:468px;top:76px}
.header-phone{left:914px;top:76px}

/* nav */
.main-nav{left:0;top:123px;width:1200px;height:49px;background:linear-gradient(var(--orange-light),var(--orange));display:flex;padding-left:135px}
.main-nav a{color:var(--white);text-decoration:none;font-family:'Lato',sans-serif;font-size:13px;padding:0 10px;line-height:49px;text-transform:uppercase}
.main-nav a.active{background:#2a2a2a;padding:0 17px}

/* hero */
.hero{left:0;top:172px;width:1200px;height:470px;background:linear-gradient(120deg,#4a3b3a,#2d2a3e 50%,#3b2a3a)}
.hero h1{position:absolute;left:0;top:150px;width:1200px;text-align:center;color:var(--white);font-family:'Montserrat',sans-serif;font-weight:600;font-size:43px;line-height:50px;letter-spacing:1px}
.arrow-btn{position:absolute;width:48px;height:48px;border:2px solid var(--white);border-radius:50%}
.arrow-btn svg{position:absolute;left:12px;top:12px}

/* featured */
.featured{left:146px;top:671px;width:910px;height:334px;background:linear-gradient(135deg,#3a2f3a,#5a3c5a 55%,#2f3a4a);text-align:center;color:var(--white)}
.featured h2{margin-top:80px;font-family:'Montserrat',sans-serif;font-weight:500;font-size:31px;letter-spacing:2px}
.featured p{width:590px;margin:12px auto 0;font-size:20px;line-height:24px}
.btn{display:inline-block;margin-top:18px;background:var(--orange);color:var(--white);font-size:15px;padding:10px 30px;text-transform:uppercase}

/* costumes */
.costumes{left:0;top:1034px;width:1200px;height:481px;background:linear-gradient(#e5e5e5,#ededed)}
.costumes h2{position:absolute;top:38px;width:1200px;text-align:center;font-family:'Montserrat',sans-serif;font-weight:500;font-size:26px;letter-spacing:1px}
.card{position:absolute;top:95px;width:288px;height:322px;background:var(--white)}
.card .photo{position:absolute;left:60px;top:8px;width:168px;height:266px;border-radius:4px}
.card .label{position:absolute;left:0;bottom:0;width:100%;height:48px;line-height:48px;text-align:center;color:var(--white);font-size:21px;text-transform:uppercase}
.label.green{background:linear-gradient(var(--green-light),var(--green))}
.label.orange{background:linear-gradient(var(--orange-light),var(--orange))}
.chev{position:absolute;top:228px}

/* category grid */
.tile{position:absolute;overflow:hidden}
.tile .caption{position:absolute;left:0;bottom:0;width:100%;height:50px;line-height:50px;text-align:center;color:var(--white);font-size:18px;text-transform:uppercase;background:var(--caption)}
.tile .caption.orange{background:linear-gradient(rgba(251,176,52,.9),var(--orange))}
.tile .caption.green{background:linear-gradient(var(--green-light),var(--green));height:42px;line-height:42px}

/* footer */
.footer-top{left:0;top:1969px;width:1200px;height:147px;background:var(--black);color:var(--white)}
.footer-address{left:140px;top:42px;font-weight:400;font-size:17px}
.footer-phone{left:140px;top:88px;font-weight:400;font-size:17px}
.footer-social{left:572px;top:46px}
.footer-social span{width:32px;height:32px}
.review{left:757px;top:36px}
.stars{display:flex;gap:4px}
.review p{margin-top:8px;font-style:italic;font-size:15px;color:#ddd}
.review small{display:block;margin-top:5px;font-size:13px;color:#bbb;padding-left:3px}
.footer-bottom{left:0;top:2116px;width:1200px;height:112px;background:var(--footer-dark);text-align:center;color:var(--white)}
.footer-nav{margin-top:36px;display:flex;justify-content:center;gap:20px}
.footer-nav a{color:var(--white);text-decoration:none;font-size:13px;text-transform:uppercase}
.copyright{margin-top:14px;font-size:11px;color:#bbb}
</style>
</head>
<body>

<header class="abs site-header">
  <div class="abs brand"><span class="brand-dot"></span>Guiseworks</div>
  <div class="abs social header-social"><span></span><span></span><span></span><span></span><span></span><span></span></div>
  <div class="abs contact-line header-address">
    <svg width="14" height="20" viewBox="0 0 14 20"><path d="M7 0a7 7 0 0 1 7 7c0 5-7 13-7 13S0 12 0 7a7 7 0 0 1 7-7z" fill="#7dc242"/><circle cx="7" cy="7" r="2.6" fill="#000"/></svg>
    418 Larkmoor Ave. N Fenwick, MN 55812
  </div>
  <div class="abs contact-line header-phone">
    <svg width="18" height="18" viewBox="0 0 24 24"><path d="M6.6 10.8a15 15 0 0 0 6.6 6.6l2.2-2.2a1 1 0 0 1 1-.25 11.4 11.4 0 0 0 3.6.57 1 1 0 0 1 1 1V20a1 1 0 0 1-1 1A17 17 0 0 1 3 4a1 1 0 0 1 1-1h3.5a1 1 0 0 1 1 1c0 1.25.2 2.45.57 3.57a1 1 0 0 1-.25 1z" fill="#7dc242"/></svg>
    555-302-7741
  </div>
</header>

<nav class="abs main-nav">
  <a class="active" href="#">Home</a><a href="#">About Us</a><a href="#">Ordering</a><a href="#">Merchandise</a><a href="#">Videos</a><a href="#">Holiday</a><a href="#">Renaissance</a><a href="#">Decade</a><a href="#">Lingerie Boutique</a><a href="#">Contact Us</a>
</nav>

<section class="abs hero" role="img" aria-label="Photo of costumed party-goers in skull and vampire makeup">
  <h1>LARGEST SELECTION OF<br>COSTUMES &amp; ACCESSORIES</h1>
  <span class="arrow-btn" style="left:124px;top:186px"><svg width="20" height="20" viewBox="0 0 20 20"><path d="M12 4 6 10l6 6" stroke="#fff" stroke-width="2.5" fill="none"/></svg></span>
  <span class="arrow-btn" style="left:1028px;top:186px"><svg width="20" height="20" viewBox="0 0 20 20"><path d="m8 4 6 6-6 6" stroke="#fff" stroke-width="2.5" fill="none"/></svg></span>
</section>

<section class="abs featured" role="img" aria-label="Store interior with racks of colourful costume accessories">
  <h2>FEATURED</h2>
  <p>Aenean porttitor eros vel dolor Donec convallis pede venenatis nibh Duis quam Nam eget lacus Aliquam erat</p>
  <span class="btn">Read More</span>
</section>

<section class="abs costumes">
  <h2>COSTUMES</h2>
  <svg class="chev" style="left:108px" width="22" height="40" viewBox="0 0 22 40"><path d="M19 3 4 20l15 17" stroke="#999" stroke-width="3" fill="none"/></svg>
  <div class="card" style="left:140px">
    <div class="photo" role="img" aria-label="Model in a green holiday leprechaun costume" style="background:linear-gradient(#3a9a3a,#2a5a2a)"></div>
    <div class="label green">Holiday</div>
  </div>
  <div class="card" style="left:453px">
    <div class="photo" role="img" aria-label="Model in a renaissance gown" style="background:linear-gradient(#6a2a3a,#b07a3a)"></div>
    <div class="label orange">Renaissance</div>
  </div>
  <div class="card" style="left:766px">
    <div class="photo" role="img" aria-label="Model in a 1920s gangster dress" style="background:linear-gradient(#333,#1a1f1a)"></div>
    <div class="label green">Decade</div>
  </div>
  <svg class="chev" style="left:1058px" width="22" height="40" viewBox="0 0 22 40"><path d="m3 3 15 17L3 37" stroke="#999" stroke-width="3" fill="none"/></svg>
</section>

<div class="tile" style="left:140px;top:1567px;width:404px;height:346px;background:linear-gradient(#6a6a6e,#8a7a7a)" role="img" aria-label="Two models in lace lingerie sets">
  <div class="caption">Lingerie Boutique</div>
</div>
<div class="tile" style="left:555px;top:1567px;width:247px;height:346px;background:linear-gradient(#3a2a22,#6a4a2a)" role="img" aria-label="Display shelves of gifts and scented oils">
  <div class="caption orange">Gifts and Oils</div>
</div>
<div class="tile" style="left:812px;top:1567px;width:248px;height:170px;background:#fff;border:1px solid #ccc" role="img" aria-label="Model wearing a black bob wig">
  <div class="caption green">Wigs</div>
</div>
<div class="tile" style="left:812px;top:1745px;width:248px;height:168px;background:linear-gradient(#3a3a4a,#4a3a3a)" role="img" aria-label="Makeup aisle in the store">
  <div class="caption">Makeup</div>
</div>

<footer>
  <div class="abs footer-top">
    <div class="abs contact-line footer-address">
      <svg width="13" height="18" viewBox="0 0 14 20"><path d="M7 0a7 7 0 0 1 7 7c0 5-7 13-7 13S0 12 0 7a7 7 0 0 1 7-7z" fill="#fff"/><circle cx="7" cy="7" r="2.6" fill="#000"/></svg>
      418 Larkmoor Ave. N Fenwick, MN 55812
    </div>
    <div class="abs contact-line footer-phone">
      <svg width="16" height="16" viewBox="0 0 24 24"><path d="M6.6 10.8a15 15 0 0 0 6.6 6.6l2.2-2.2a1 1 0 0 1 1-.25 11.4 11.4 0 0 0 3.6.57 1 1 0 0 1 1 1V20a1 1 0 0 1-1 1A17 17 0 0 1 3 4a1 1 0 0 1 1-1h3.5a1 1 0 0 1 1 1c0 1.25.2 2.45.57 3.57a1 1 0 0 1-.25 1z" fill="#fff"/></svg>
      555-302-7741
    </div>
    <div class="abs social footer-social"><span></span><span></span><span></span><span></span></div>
    <div class="abs review">
      <div class="stars">
        <svg width="24" height="23" viewBox="0 0 24 23"><path d="m12 0 3.5 7.5 8.5 1-6.3 5.7 1.7 8.3L12 18.3 4.6 22.5l1.7-8.3L0 8.5l8.5-1z" fill="#f6c400"/></svg>
        <svg width="24" height="23" viewBox="0 0 24 23"><path d="m12 0 3.5 7.5 8.5 1-6.3 5.7 1.7 8.3L12 18.3 4.6 22.5l1.7-8.3L0 8.5l8.5-1z" fill="#f6c400"/></svg>
        <svg width="24" height="23" viewBox="0 0 24 23"><path d="m12 0 3.5 7.5 8.5 1-6.3 5.7 1.7 8.3L12 18.3 4.6 22.5l1.7-8.3L0 8.5l8.5-1z" fill="#f6c400"/></svg>
        <svg width="24" height="23" viewBox="0 0 24 23"><path d="m12 0 3.5 7.5 8.5 1-6.3 5.7 1.7 8.3L12 18.3 4.6 22.5l1.7-8.3L0 8.5l8.5-1z" fill="#f6c400"/></svg>
        <svg width="24" height="23" viewBox="0 0 24 23"><path d="m12 0 3.5 7.5 8.5 1-6.3 5.7 1.7 8.3L12 18.3 4.6 22.5l1.7-8.3L0 8.5l8.5-1z" fill="#f6c400"/></svg>
      </div>
      <p>Class aptent taciti sociosqu ad litora torquent</p>
      <small>By Author Name</small>
    </div>
  </div>
  <div class="abs footer-bottom">
    <nav class="footer-nav">
      <a href="#">Home</a><a href="#">About Us</a><a href="#">Ordering</a><a href="#">Merchandise</a><a href="#">Videos</a><a href="#">Holiday</a><a href="#">Renaissance</a><a href="#">Decade</a><a href="#">Lingerie Boutique</a><a href="#">Contact Us</a>
    </nav>
    <p class="copyright">© 2018 Company Name &nbsp;All right reserved &nbsp;Terms of Use</p>
  </div>
</footer>

</body>
</html>
```